Property risk and finance brokerage company needs a business card design

Tarn Financial requires a business card design. Please integrate existing logo (refer uploaded file).
hex codes used on logo #002649 #008ED6 #444F51 #ADAFAA
font used - Cinzel
Contact information
Roslyn Venterelli
Director
Mobile: 0471 385 902
email: r.venterelli@tarnfinancial.com.au
website: www.tarnfinancial.com.au
CRN : 815390
PO Box 547
Canterbury, Victoria, 3126
Horizontal orientation please

```html
<!DOCTYPE html>
<html lang="en">
<head>
<meta charset="utf-8">
<title>Tarn Financial – Business Card</title>
<link rel="stylesheet" href="https://fonts.googleapis.com/css2?family=Open+Sans:wght@400;600;700&display=swap">
<style>
  :root {
    --navy: #002649;
    --brand-blue: #1f5a96;
    --deep-blue: #0d3a6e;
    --bright-blue: #008ED6;
    --slate: #444F51;
    --stone: #ADAFAA;
    --paper: #ffffff;
    --backdrop: #eceeef;
    --text-dark: #3a3f42;
  }
  * { box-sizing: border-box; margin: 0; padding: 0; }
  html, body {
    width: 1200px; height: 720px; overflow: hidden;
    background: var(--backdrop);
    font-family: "Open Sans", Arial, sans-serif;
  }
  .canvas {
    position: relative; width: 1200px; height: 720px;
    display: flex; align-items: center; justify-content: center; gap: 40px;
  }
  .card {
    position: relative; width: 540px; height: 309px;
    border-radius: 3px; overflow: hidden;
    box-shadow: 0 6px 18px rgba(0,0,0,.18);
  }
  /* front */
  .card-front { background: var(--paper); }
  .card-front .bands { position: absolute; inset: 0; }
  .brand {
    position: absolute; left: 40px; top: 44px;
    display: flex; align-items: center; gap: 12px;
  }
  .brand-dot { width: 34px; height: 34px; border-radius: 50%; background: var(--brand-blue); }
  .brand-name {
    font-weight: 600; font-size: 28px; color: var(--navy);
    letter-spacing: .5px;
  }
  .person { position: absolute; right: 40px; top: 56px; text-align: right; }
  .person-name { font-weight: 700; font-size: 17px; color: var(--navy); }
  .person-role { font-size: 11px; color: var(--slate); margin-top: 1px; }
  .contacts {
    position: absolute; left: 40px; top: 150px;
    list-style: none; font-size: 12.5px; color: var(--text-dark);
  }
  .contacts li { display: flex; align-items: center; gap: 8px; line-height: 21px; }
  .contacts svg { width: 12px; height: 12px; flex: none; }
  .address {
    position: absolute; left: 40px; bottom: 16px;
    font-size: 12.5px; color: var(--paper);
  }
  /* back */
  .card-back {
    background: radial-gradient(ellipse at 50% 42%, #2a7fc4 0%, #155394 45%, #0a3463 100%);
  }
  .back-mark {
    position: absolute; left: 0; right: 0; top: 80px;
    display: flex; align-items: center; justify-content: center; gap: 12px;
  }
  .back-mark .brand-dot { background: var(--paper); width: 30px; height: 30px; }
  .back-mark .brand-name { color: var(--paper); font-size: 26px; }
  .back-url {
    position: absolute; right: 40px; bottom: 34px;
    font-size: 17px; color: var(--paper); letter-spacing: .6px;
  }
</style>
</head>
<body>
<main class="canvas">
  <section class="card card-front" aria-label="Card front">
    <svg class="bands" viewBox="0 0 540 309" preserveAspectRatio="none" aria-hidden="true">
      <defs>
        <linearGradient id="bandFill" x1="0" y1="0" x2="1" y2="0">
          <stop offset="0" stop-color="#0d3a6e"/>
          <stop offset="1" stop-color="#1f5a96"/>
        </linearGradient>
      </defs>
      <polygon points="0,252 540,214 540,219 0,256" fill="#1f5a96"/>
      <polygon points="0,262 540,226 540,309 0,309" fill="url(#bandFill)"/>
    </svg>
    <div class="brand">
      <span class="brand-dot"></span>
      <span class="brand-name">Tarn Financial</span>
    </div>
    <div class="person">
      <p class="person-name">Roslyn Venterelli</p>
      <p class="person-role">Director</p>
    </div>
    <ul class="contacts">
      <li>
        <svg viewBox="0 0 12 12"><rect x="3" y="0.5" width="6" height="11" rx="1.2" fill="#1f5a96"/><rect x="4" y="2" width="4" height="6" fill="#fff"/></svg>
        0471 385 902
      </li>
      <li>
        <svg viewBox="0 0 12 12"><rect x="0.5" y="2" width="11" height="8" rx="1" fill="#1f5a96"/><path d="M1 2.8 6 6.8 11 2.8" stroke="#fff" stroke-width="1" fill="none"/></svg>
        r.venterelli@tarnfinancial.com.au
      </li>
      <li>
        <svg viewBox="0 0 12 12"><circle cx="6" cy="6" r="5.3" fill="#1f5a96"/><path d="M1 6h10M6 1c-2.4 2.8-2.4 7.2 0 10M6 1c2.4 2.8 2.4 7.2 0 10" stroke="#fff" stroke-width=".8" fill="none"/></svg>
        www.tarnfinancial.com.au
      </li>
    </ul>
    <p class="address">PO Box 547 Ashvale, VIC 3127</p>
  </section>

  <section class="card card-back" aria-label="Card back">
    <div class="back-mark">
      <span class="brand-dot"></span>
      <span class="brand-name">Tarn Financial</span>
    </div>
    <p class="back-url">www.tarnfinancial.com.au</p>
  </section>
</main>
</body>
</html>
```